Easy Marinade Labels for Butchery Store

Need a set of labels designed for a Butchery Shop. They will sit in the top left corner of the packets as a triangle (7cm each side). Easy because the only major requirement is the label name and some small text saying "Please ask in store to see spec sheet for ingredients". Extra points for finding a fun way to incorporate the logo and/or images of food (garlic bulbs, chilli, spices ect) to enhance the label. List of Marinade Names below: GarlicPepper Mint & RosemarySatayBBQChilli Plum & GingerSundried Tomato & BasilBuffaloHoney SoyHoi-SinPer PeriSpicy CajunTeriyakiBlack Bean Ive also attached the logo and an example of how the label might sit on a packet of meat. Thanks

Target Market(s)

Butchery Deli Shop Customers

Industry/Entity Type

Food Store

Font styles to use
Serif
Sans Serif
Decorative
Other font styles liked:
• Fun font that isn't a generic Quanderel Font?

Colors

Designer to choose colors to be used in the design.

Requirements
Must have
• Product Name
• Small text saying "Please ask in store to see spec sheet for ingredients"
Nice to have
• Photos of ingredients that would match that type of marinade - Chilli, Garlic, Spices.
• Brava Vell Logo - not essential if it doesn't look good on the label / doesn't fit.

```html
<!DOCTYPE html>
<html lang="en">
<head>
<meta charset="utf-8">
<title>Brava Vell Marinade Labels</title>
<link rel="stylesheet" href="https://fonts.googleapis.com/css2?family=Ultra&family=Tinos:wght@400;700&family=Open+Sans:wght@400&display=swap">
<style>
  :root {
    --bg-centre: #ffffff;
    --bg-edge: #c3c9ce;
    --cream: #f7f3ea;
    --brand-red: #b5121b;
    --ink: #3a2f2a;
    --strip-ink: #5a4640;
    --tomato: #c8141b;
    --tomato-frame: #c8141b;
    --tomato-rim: #5fb44a;
    --garlic-frame: #7d6760;
    --garlic-ink: #735a50;
    --peri-frame: #c8141b;
    --bean: #2b2b2b;
    --bean-frame: #1e1e1e;
    --bean-rim: #47b046;
    --pepper-frame: #2c2c2c;
    --mint: #66755a;
    --mint-frame: #9ad9bc;
  }
  html, body {
    margin: 0;
    width: 1200px;
    height: 923px;
    overflow: hidden;
  }
  body {
    background: radial-gradient(ellipse at 50% 45%, var(--bg-centre) 30%, var(--bg-edge) 100%);
  }
  .label-sheet { display: block; width: 1200px; height: 923px; }

  .label .rim-outer { fill: url(#gold); }
  .label .rim-colour { fill: var(--frame); }
  .label .rim-accent { fill: var(--rim, var(--frame)); }
  .label .face { fill: var(--cream); }
  .label .band { fill: var(--band); }
  .label .strip { fill: var(--cream); stroke: var(--frame); stroke-width: 1; }

  .brand-name {
    font-family: "Tinos", "Times New Roman", serif;
    font-weight: 700;
    font-size: 24px;
    fill: var(--brand-red);
    letter-spacing: 0.5px;
  }
  .marinated {
    font-family: "Tinos", "Times New Roman", serif;
    font-size: 19px;
    fill: var(--ink);
  }
  .flavour-name {
    font-family: "Ultra", "Rockwell Extra Bold", "Georgia", serif;
    font-size: 23px;
    fill: #ffffff;
  }
  .label--garlic .flavour-name { fill: var(--garlic-ink); }
  .spec-note {
    font-family: "Open Sans", Arial, sans-serif;
    font-size: 11.5px;
    fill: var(--strip-ink);
  }

  .label--tomato { --frame: var(--tomato-frame); --rim: var(--tomato-rim); --band: var(--tomato); }
  .label--garlic { --frame: var(--garlic-frame); --band: url(#garlicBand); }
  .label--peri   { --frame: var(--peri-frame); --rim: #f08a16; --band: url(#periBand); }
  .label--bean   { --frame: var(--bean-frame); --rim: var(--bean-rim); --band: var(--bean); }
  .label--pepper { --frame: var(--pepper-frame); --rim: #9a9a9a; --band: url(#pepperBand); }
  .label--mint   { --frame: var(--mint-frame); --rim: #6ba88b; --band: var(--mint); }
</style>
</head>
<body>
<svg class="label-sheet" viewBox="0 0 1300 1000" xmlns="http://www.w3.org/2000/svg">
  <defs>
    <linearGradient id="gold" x1="0" y1="0" x2="1" y2="1">
      <stop offset="0" stop-color="#8a7440"/>
      <stop offset="0.5" stop-color="#e6d78a"/>
      <stop offset="1" stop-color="#8a7440"/>
    </linearGradient>
    <linearGradient id="garlicBand" x1="0" y1="0" x2="1" y2="0">
      <stop offset="0" stop-color="#c9b897"/>
      <stop offset="1" stop-color="#a99473"/>
    </linearGradient>
    <linearGradient id="periBand" x1="0" y1="0" x2="1" y2="0">
      <stop offset="0" stop-color="#f07a10"/>
      <stop offset="0.5" stop-color="#d01a10"/>
      <stop offset="1" stop-color="#f07a10"/>
    </linearGradient>
    <linearGradient id="pepperBand" x1="0" y1="0" x2="1" y2="0">
      <stop offset="0" stop-color="#c9c9c9"/>
      <stop offset="0.5" stop-color="#3a3a3a"/>
      <stop offset="1" stop-color="#c9c9c9"/>
    </linearGradient>
  </defs>

  <g class="label label--tomato" transform="translate(137 118)">
    <polygon class="rim-outer" points="242,0 484,240 0,240"/>
    <polygon class="rim-colour" points="242,8 474,236 10,236"/>
    <polygon class="rim-accent" points="242,16 462,232 22,232"/>
    <polygon class="face" points="242,22 452,228 32,228"/>
    <polygon class="band" points="116,152 368,152 426,207 58,207"/>
    <rect class="strip" x="50" y="210" width="384" height="16"/>
    <circle role="img" aria-label="Ripe tomato with basil leaves" cx="242" cy="68" r="21" fill="#c8141b"/>
    <text class="brand-name" x="242" y="118" text-anchor="middle">BRAVA VELL</text>
    <text class="marinated" x="242" y="146" text-anchor="middle">marinated with</text>
    <text class="flavour-name" x="242" y="176" text-anchor="middle">Sundried Tomato</text>
    <text class="flavour-name" x="242" y="200" text-anchor="middle">&amp; Basil</text>
    <text class="spec-note" x="242" y="223" text-anchor="middle">PLEASE ASK IN STORE TO SEE SPEC SHEET FOR INGREDIENTS</text>
  </g>

  <g class="label label--garlic" transform="translate(679 118)">
    <polygon class="rim-outer" points="242,0 484,240 0,240"/>
    <polygon class="rim-colour" points="242,8 474,236 10,236"/>
    <polygon class="face" points="242,18 458,230 26,230"/>
    <polygon class="band" points="116,152 368,152 426,207 58,207"/>
    <rect class="strip" x="50" y="210" width="384" height="16"/>
    <ellipse role="img" aria-label="Garlic bulbs and cloves" cx="242" cy="68" rx="22" ry="21" fill="#ece3cf"/>
    <text class="brand-name" x="242" y="118" text-anchor="middle">BRAVA VELL</text>
    <text class="marinated" x="242" y="146" text-anchor="middle">marinated with</text>
    <text class="flavour-name" x="242" y="187" text-anchor="middle">Garlic Sprinkle</text>
    <text class="spec-note" x="242" y="223" text-anchor="middle">PLEASE ASK IN STORE TO SEE SPEC SHEET FOR INGREDIENTS</text>
  </g>

  <g class="label label--peri" transform="translate(137 378)">
    <polygon class="rim-outer" points="242,0 484,240 0,240"/>
    <polygon class="rim-colour" points="242,8 474,236 10,236"/>
    <polygon class="rim-accent" points="242,16 462,232 22,232"/>
    <polygon class="face" points="242,22 452,228 32,228"/>
    <polygon class="band" points="112,153 372,153 426,210 58,210"/>
    <rect class="strip" x="50" y="212" width="384" height="15"/>
    <ellipse role="img" aria-label="Red chilli peppers with garlic" cx="242" cy="70" rx="24" ry="18" fill="#d8401a"/>
    <text class="brand-name" x="242" y="118" text-anchor="middle">BRAVA VELL</text>
    <text class="marinated" x="242" y="147" text-anchor="middle">marinated with</text>
    <text class="flavour-name" x="242" y="189" text-anchor="middle">Peri Peri</text>
    <text class="spec-note" x="242" y="224" text-anchor="middle">PLEASE ASK IN STORE TO SEE SPEC SHEET FOR INGREDIENTS</text>
  </g>

  <g class="label label--bean" transform="translate(679 378)">
    <polygon class="rim-outer" points="242,0 484,240 0,240"/>
    <polygon class="rim-colour" points="242,8 474,236 10,236"/>
    <polygon class="rim-accent" points="242,16 462,232 22,232"/>
    <polygon class="face" points="242,22 452,228 32,228"/>
    <polygon class="band" points="112,153 372,153 426,210 58,210"/>
    <rect class="strip" x="50" y="212" width="384" height="15"/>
    <ellipse role="img" aria-label="Black beans" cx="242" cy="68" rx="22" ry="21" fill="#1f1f1f"/>
    <text class="brand-name" x="242" y="118" text-anchor="middle">BRAVA VELL</text>
    <text class="marinated" x="242" y="147" text-anchor="middle">marinated with</text>
    <text class="flavour-name" x="242" y="189" text-anchor="middle">Black Bean Sauce</text>
    <text class="spec-note" x="242" y="224" text-anchor="middle">PLEASE ASK IN STORE TO SEE SPEC SHEET FOR INGREDIENTS</text>
  </g>

  <g class="label label--pepper" transform="translate(137 643)">
    <polygon class="rim-outer" points="242,0 484,240 0,240"/>
    <polygon class="rim-colour" points="242,8 474,236 10,236"/>
    <polygon class="rim-accent" points="242,16 462,232 22,232"/>
    <polygon class="face" points="242,22 452,228 32,228"/>
    <polygon class="band" points="112,153 372,153 426,210 58,210"/>
    <rect class="strip" x="50" y="212" width="384" height="15"/>
    <circle role="img" aria-label="Pepper shaker" cx="242" cy="68" r="21" fill="#2a2a2a"/>
    <text class="brand-name" x="242" y="118" text-anchor="middle">BRAVA VELL</text>
    <text class="marinated" x="242" y="147" text-anchor="middle">marinated with</text>
    <text class="flavour-name" x="242" y="189" text-anchor="middle">Pepper Sprinkle</text>
    <text class="spec-note" x="242" y="224" text-anchor="middle">PLEASE ASK IN STORE TO SEE SPEC SHEET FOR INGREDIENTS</text>
  </g>

  <g class="label label--mint" transform="translate(679 643)">
    <polygon class="rim-outer" points="242,0 484,240 0,240"/>
    <polygon class="rim-colour" points="242,8 474,236 10,236"/>
    <polygon class="rim-accent" points="242,16 462,232 22,232"/>
    <polygon class="face" points="242,22 452,228 32,228"/>
    <polygon class="band" points="112,153 372,153 426,210 58,210"/>
    <rect class="strip" x="50" y="212" width="384" height="15"/>
    <ellipse role="img" aria-label="Sprigs of mint and rosemary" cx="242" cy="70" rx="24" ry="18" fill="#5f9a6c"/>
    <text class="brand-name" x="242" y="118" text-anchor="middle">BRAVA VELL</text>
    <text class="marinated" x="242" y="147" text-anchor="middle">marinated with</text>
    <text class="flavour-name" x="242" y="189" text-anchor="middle">Mint &amp; Rosemary</text>
    <text class="spec-note" x="242" y="224" text-anchor="middle">PLEASE ASK IN STORE TO SEE SPEC SHEET FOR INGREDIENTS</text>
  </g>
</svg>
</body>
</html>
```